Business Card Design - Construction Company

Tarrowin Construction is in need of a sharp, modern business card design that has an architectural/high fashion feel.

We are looking for a two sided card.

One side simple dark grey/black with some texture in the background. e.g. (a mosaic of simple interconnecting shapes or a shadow of the logo.) Something to draw attention and create interest.It will need to feature a large Tarrowin construction logo (files attached) in metallic gradient or plain white.

The other side should contain all of our information:

(in largest text)
Name of person
Tarrowin Construction Pty. Ltd.

Licensed builders specialising in:
- Bathrooms
- Kitchens
- Commercial interiors

(mid sized text)
Phone number
Fax number
person@tarrowinconstruction.example.au
www. tarrowinconstruction.example.au

(smaller text)
ABN: 62407938215
BSA license: xxx-xxxx
PO Box 8641 Kellsmoor QLD 4019 (address)

Target Market(s)

professional home and business owners

Industry/Entity Type

Construction

Requirements
Must have
• Must be bold, professional looking and modern.
Nice to have
• We are undecided as to what kind of printing we will go with.
Definitely square edged.
Probably high quality satin card.
We are also interested in designs that would work well on transparent or translucent plastic.
Ideally we would print two versions.
Should not have
• Nothing with an antique feel.
No wild colours. Small amounts of colour can be good in the right place.

```html
<!DOCTYPE html>
<html lang="en">
<head>
<meta charset="utf-8">
<title>Tarrowin Construction – Business Cards</title>
<link rel="stylesheet" href="https://fonts.googleapis.com/css2?family=Source+Sans+3:ital,wght@0,400;0,600;0,700;1,400;1,700&display=swap">
<style>
  :root {
    --page: #ffffff;
    --card: #ffffff;
    --ink: #2e2e2e;
    --ink-soft: #555555;
    --brand-grey: #6f6f6f;
    --mosaic-light: #c9c9c9;
    --mosaic-mid: #9a9a9a;
    --mosaic-dark: #5a5a5a;
    --shadow: rgba(0, 0, 0, 0.35);
  }
  * { box-sizing: border-box; margin: 0; padding: 0; }
  html, body {
    width: 1161px; height: 1200px; overflow: hidden;
    background: var(--page);
    font-family: "Source Sans 3", sans-serif;
    color: var(--ink);
  }
  .canvas { position: relative; width: 1161px; height: 1200px; }

  .card {
    position: absolute;
    background: var(--card);
    box-shadow: 6px 8px 14px var(--shadow);
    overflow: hidden;
  }
  .card--front { left: 72px; top: 71px; width: 1018px; height: 487px; }
  .card--back  { left: 172px; top: 632px; width: 890px; height: 495px; }

  .ground { position: absolute; left: 0; top: 0; width: 100%; height: 100%; }

  .brand {
    position: absolute;
    display: flex; flex-direction: column; align-items: center;
    transform: translateX(-50%);
  }
  .brand__dot { border-radius: 50%; background: var(--brand-grey); }
  .brand__name {
    font-weight: 700; letter-spacing: 1px;
    color: var(--brand-grey); white-space: nowrap;
  }
  .card--front .brand { left: 440px; top: 42px; }
  .card--front .brand__dot { width: 90px; height: 90px; }
  .card--front .brand__name { margin-top: 30px; font-size: 30px; line-height: 34px; }

  .card--back .brand { left: 435px; top: 36px; }
  .card--back .brand__dot { width: 100px; height: 100px; }
  .card--back .brand__name { margin-top: 18px; font-size: 28px; line-height: 32px; }

  .pendant {
    position: absolute;
    border-radius: 16px;
    background:
      linear-gradient(90deg, rgba(255,255,255,0.35), rgba(255,255,255,0) 30%, rgba(0,0,0,0) 70%, rgba(0,0,0,0.2)),
      radial-gradient(ellipse at 50% 50%, var(--mosaic-dark) 0%, var(--mosaic-mid) 45%, var(--mosaic-light) 100%);
    box-shadow: 0 0 0 3px #e4e4e4, 2px 3px 6px rgba(0,0,0,0.3);
  }
  .card--front .pendant { left: 365px; top: 227px; width: 144px; height: 252px; }
  .card--back .pendant { left: 360px; top: 214px; width: 151px; height: 270px; }

  .services {
    position: absolute; right: 675px; top: 302px;
    list-style: none; text-align: right;
    font-size: 17px; line-height: 24px; color: var(--ink);
  }
  .services li::after {
    content: ""; display: inline-block;
    width: 8px; height: 8px; margin-left: 9px;
    background: var(--ink); vertical-align: 1px;
  }

  .contact { position: absolute; left: 544px; top: 233px; color: var(--ink); }
  .contact__name { font-size: 21px; font-weight: 700; font-style: italic; line-height: 25px; }
  .contact__company { font-size: 16px; font-style: italic; line-height: 21px; color: var(--ink-soft); }
  .contact__lines { margin-top: 15px; font-size: 17px; line-height: 24px; }
  .contact__lines b { font-weight: 700; }
  .gap { display: inline-block; width: 14px; }
</style>
</head>
<body>
<main class="canvas">

  <section class="card card--front" aria-label="Business card, information side">
    <svg class="ground" viewBox="0 0 1018 487" preserveAspectRatio="none" role="img" aria-label="Grey stone mosaic ground forming a gentle arc along the bottom">
      <defs>
        <linearGradient id="groundFront" x1="0" y1="0" x2="0" y2="1">
          <stop offset="0" stop-color="#b5b5b5"/>
          <stop offset="1" stop-color="#7d7d7d"/>
        </linearGradient>
      </defs>
      <path d="M0 473 Q509 341 1018 473 L1018 487 L0 487 Z" fill="url(#groundFront)"/>
    </svg>

    <div class="brand">
      <span class="brand__dot"></span>
      <span class="brand__name">Tarrowin Construction</span>
    </div>

    <div class="pendant" role="img" aria-label="Ornamental mosaic tile panel in greys"></div>

    <ul class="services">
      <li>Bathrooms</li>
      <li>Kitchens</li>
      <li>Commercial interiors</li>
    </ul>

    <div class="contact">
      <p class="contact__name">Name Name</p>
      <p class="contact__company">Tarrowin Construction Pty. Ltd.</p>
      <p class="contact__lines">
        <b>T:</b> 00 0000000<span class="gap"></span><b>F:</b> 00 00000000<br>
        person@tarrowinconstruction.example.au<br>
        www. tarrowinconstruction.example.au
      </p>
    </div>
  </section>

  <section class="card card--back" aria-label="Business card, brand side">
    <svg class="ground" viewBox="0 0 890 495" preserveAspectRatio="none" role="img" aria-label="Grey stone mosaic ground forming a gentle arc along the bottom">
      <defs>
        <linearGradient id="groundBack" x1="0" y1="0" x2="0" y2="1">
          <stop offset="0" stop-color="#b5b5b5"/>
          <stop offset="1" stop-color="#7d7d7d"/>
        </linearGradient>
      </defs>
      <path d="M0 455 Q445 367 890 455 L890 495 L0 495 Z" fill="url(#groundBack)"/>
    </svg>

    <div class="brand">
      <span class="brand__dot"></span>
      <span class="brand__name">Tarrowin Construction</span>
    </div>

    <div class="pendant" role="img" aria-label="Ornamental mosaic tile panel in greys"></div>
  </section>

</main>
</body>
</html>
```